Business Card & Stationery Design for a General Contracting Company
Brenwick Contracting Limited
Tolvane Perdo
Managing Director
No 7 Marlowe Crescent, Elmsby
brenwickcontracting@quillpost.net
The Company is involved in supply and transport of aggregate materials and heavy equipment rental at present. Furthermore we recently had a project for the logo design of our Company on this website and we would like to incorporate this logo into our stationery designs and business cards. Please see the links below; Our design project; http://orders.markcraftstudio.net/contests/logo-for-a-general-contracting-company The logo chosen; http://orders.markcraftstudio.net/drafts/display/contest/512093/draft/e7d4b58213690ab1c5f93d478ee2bb718204617

```html
<!DOCTYPE html>
<html lang="en">
<head>
<meta charset="utf-8">
<title>Brenwick Contracting Limited – Business Card</title>
<link href="https://fonts.googleapis.com/css2?family=Roboto+Condensed:wght@700&family=Open+Sans:ital,wght@0,400;0,600;1,600&display=swap" rel="stylesheet">
<style>
  :root {
    --bg: #d9dadb;
    --card: #ffffff;
    --blue: #1f5fa8;
    --red: #c0202e;
    --ink: #3d4450;
    --muted: #6b7280;
  }
  * { box-sizing: border-box; margin: 0; padding: 0; }
  html, body { width: 1200px; height: 984px; overflow: hidden; }
  body {
    background: var(--bg);
    font-family: "Open Sans", sans-serif;
    position: relative;
  }
  .card {
    position: absolute;
    left: 220px;
    width: 760px;
    height: 434px;
    background: var(--card);
    border-radius: 26px;
    overflow: hidden;
    box-shadow: 0 6px 18px rgba(0,0,0,0.12);
  }
  .card--back { top: 36px; }
  .card--front { top: 514px; }

  .brand { position: absolute; display: flex; align-items: center; gap: 14px; }
  .brand__dot { border-radius: 50%; background: var(--blue); flex: none; }
  .brand__name {
    font-family: "Roboto Condensed", sans-serif;
    font-weight: 700;
    color: var(--blue);
    text-transform: uppercase;
    line-height: 1.05;
  }
  .card--back .brand { left: 0; right: 0; top: 150px; justify-content: center; }
  .card--back .brand__dot { width: 64px; height: 64px; }
  .card--back .brand__name { font-size: 34px; }
  .back-web {
    position: absolute; left: 150px; top: 300px;
    font-size: 17px; letter-spacing: 3px; color: var(--ink); font-style: italic; font-weight: 600;
  }

  .card--front .brand { left: 44px; top: 40px; }
  .card--front .brand__dot { width: 70px; height: 70px; }
  .card--front .brand__name { font-size: 36px; }

  .person { position: absolute; left: 60px; top: 160px; }
  .person__name { font-style: italic; font-weight: 600; font-size: 24px; color: var(--blue); }
  .person__title { font-size: 15px; color: var(--muted); margin-top: 2px; }
  .person__address { font-size: 15px; color: var(--ink); margin-top: 22px; }

  .contacts { position: absolute; left: 430px; top: 150px; list-style: none; }
  .contacts li { display: flex; align-items: center; gap: 10px; font-size: 15px; color: var(--ink); height: 28px; }
  .contacts svg { width: 18px; height: 18px; flex: none; }

  .waves { position: absolute; left: 0; top: 0; width: 760px; height: 434px; }
</style>
</head>
<body>
  <section class="card card--back">
    <div class="brand">
      <span class="brand__dot"></span>
      <span class="brand__name">Brenwick Contracting Limited</span>
    </div>
    <p class="back-web">www.brenwickdomain.com</p>
  </section>

  <section class="card card--front">
    <svg class="waves" viewBox="0 0 760 434" aria-hidden="true">
      <path d="M0,262 C160,345 360,372 760,350 L760,364 C360,388 160,362 0,284 Z" fill="var(--red)"/>
      <path d="M0,300 C160,382 360,404 760,384 L760,434 L0,434 Z" fill="var(--blue)"/>
    </svg>

    <div class="brand">
      <span class="brand__dot"></span>
      <span class="brand__name">Brenwick Contracting<br>Limited</span>
    </div>

    <div class="person">
      <p class="person__name">Tolvane Perdo</p>
      <p class="person__title">Managing Director</p>
      <p class="person__address">No 7 Marlowe Crescent, Elmsby</p>
    </div>

    <ul class="contacts">
      <li><svg viewBox="0 0 18 18"><circle cx="9" cy="9" r="9" fill="var(--blue)"/><path d="M6 5l2 2-1 1.2c.6 1.2 1.6 2.2 2.8 2.8L11 10l2 2-1.3 1.3C8.5 13 5 9.5 4.7 6.3Z" fill="#fff"/></svg>418-5273</li>
      <li><svg viewBox="0 0 18 18"><circle cx="9" cy="9" r="9" fill="var(--blue)"/><path d="M6 5l2 2-1 1.2c.6 1.2 1.6 2.2 2.8 2.8L11 10l2 2-1.3 1.3C8.5 13 5 9.5 4.7 6.3Z" fill="#fff"/></svg>418-6604</li>
      <li><svg viewBox="0 0 18 18"><circle cx="9" cy="9" r="9" fill="var(--blue)"/><path d="M6 5l2 2-1 1.2c.6 1.2 1.6 2.2 2.8 2.8L11 10l2 2-1.3 1.3C8.5 13 5 9.5 4.7 6.3Z" fill="#fff"/></svg>418-7391</li>
      <li><svg viewBox="0 0 18 18"><circle cx="9" cy="9" r="9" fill="var(--blue)"/><rect x="4.5" y="6" width="9" height="6.5" fill="none" stroke="#fff" stroke-width="1.2"/><path d="M4.5 6l4.5 3.6L13.5 6" fill="none" stroke="#fff" stroke-width="1.2"/></svg>brenwickcontracting@quillpost.net</li>
      <li><svg viewBox="0 0 18 18"><circle cx="9" cy="9" r="9" fill="var(--blue)"/><circle cx="9" cy="9" r="4.6" fill="none" stroke="#fff" stroke-width="1.2"/><path d="M4.4 9h9.2M9 4.4c-2 2.6-2 6.6 0 9.2M9 4.4c2 2.6 2 6.6 0 9.2" fill="none" stroke="#fff" stroke-width="1"/></svg>www.brenwickdomain.com</li>
    </ul>
  </section>
</body>
</html>
```